Flyer-Design für Initiativbewerbung
Zielgruppe
Wir sind ein Buchhaltungsbüro. Mit diesem Flyer möchten wir uns bei Steuerberater als freier Mitarbeiter bewerben als initiativ Bewerbung! Ich lade Bilder von mir selbst mit hoch um so noch persönlicher zu werden. Die Bilder können gerne bearbeitet werden und Ausschnitte gezogen werden. Es soll sehr persönlich rüber kommen
Aufgabenstellung
Flyer sollte Din A Lang sein als Endformat, also gerne auch mehrseitig und max. 20 g haben
Sie können auch Textpassagen duplizieren und auf eine Vorderseite etc machen.
Es soll persönlich wirken obwohl es ein Werbeversand. Anbei auch das Logo unserer Firma.
Ich bin auch offen das Logo in Schwarz weiß darzustellen um so vom Blau wegzukommen.
Ich lasse mich gerne überraschen.
Text
Initiativ Bewerbung freier Mitarbeiter für Ihre Kanzlei
Sehr geehrte Damen und Herren,
gerne bewerben wir uns als freier Mitarbeiter im Rahmen des

```html
<!DOCTYPE html>
<html lang="de">
<head>
<meta charset="utf-8">
<title>Initiativ Bewerbung – Flyer DIN lang</title>
<link href="https://fonts.googleapis.com/css2?family=Barlow:wght@400;500;600&display=swap" rel="stylesheet">
<style>
  :root{
    --blue:#0f5bb5;
    --blue-dark:#0b4ea8;
    --blue-light:#b3c3ea;
    --text:#1d2a3a;
    --muted:#a9b7e0;
    --paper:#ffffff;
    --bg:#ffffff;
    --photo-a:#8d8d8d;
    --photo-b:#e4e4e4;
  }
  *{box-sizing:border-box;margin:0;padding:0}
  html,body{width:1200px;height:473px;overflow:hidden;background:var(--bg)}
  body{font-family:"Barlow",Arial,sans-serif;color:var(--text);position:relative}
  .page{position:absolute;top:24px;width:200px;height:424px;background:var(--paper);
    box-shadow:2px 3px 6px rgba(0,0,0,.28);overflow:hidden}
  .page--front{left:389px}
  .page--back{left:611px}
  .top-band{height:6px;display:flex}
  .top-band span:first-child{width:50%;background:var(--blue-dark)}
  .top-band span:last-child{width:50%;background:var(--blue-light)}
  .front-header{height:55px;text-align:center;padding-top:15px}
  .front-title{font-size:11px;font-weight:600;letter-spacing:1px;color:var(--blue)}
  .front-sub{font-size:7px;letter-spacing:.6px;margin-top:4px}
  .portrait{height:248px;background:linear-gradient(100deg,var(--photo-b) 0%,var(--photo-a) 45%,var(--photo-b) 100%)}
  .mid-band{height:6px;display:flex}
  .mid-band span:first-child{width:50%;background:var(--blue-dark)}
  .mid-band span:last-child{width:50%;background:var(--blue-light)}
  .front-foot{position:absolute;left:0;right:0;bottom:0;height:109px;background:var(--blue);
    display:flex;flex-direction:column;align-items:center;justify-content:center;color:#fff}
  .brand-mark{width:16px;height:16px;background:#fff;margin-bottom:6px}
  .brand-name{font-size:16px;font-weight:400;letter-spacing:1px}
  .brand-form{font-size:5.5px;letter-spacing:5px;margin-top:2px}
  .letter{padding:44px 20px 0 20px;font-size:6.6px;line-height:12.8px}
  .salutation{color:var(--muted);margin-bottom:12px}
  .letter p{margin-bottom:12px}
  .services{border:1px solid var(--blue-light);padding:2px 8px;margin:-2px 0 14px;list-style:none}
  .services li{font-size:6.4px;letter-spacing:.3px;line-height:12.8px}
  .services li::before{content:"•";margin-right:8px}
  .signature{margin-top:26px;border-top:1px solid var(--blue-light);padding-top:3px;font-size:4px;color:var(--muted)}
  .back-foot{position:absolute;left:0;right:0;bottom:0;height:73px;background:var(--blue);color:#fff;
    text-align:center;font-size:6.8px;line-height:12.8px;padding-top:14px}
  .icon{display:inline-block;vertical-align:-1px;margin-right:2px}
</style>
</head>
<body>
  <section class="page page--front">
    <div class="top-band"><span></span><span></span></div>
    <header class="front-header">
      <h1 class="front-title">INITIATIV BEWERBUNG</h1>
      <p class="front-sub">freier Mitarbeiter für Ihre Kanzlei</p>
    </header>
    <div class="portrait" role="img" aria-label="Schwarz-Weiß-Porträtfoto des Inhabers im hellen Sakko in einem Büro"></div>
    <div class="mid-band"><span></span><span></span></div>
    <footer class="front-foot">
      <div class="brand-mark"></div>
      <div class="brand-name">KONTOWERK</div>
      <div class="brand-form">GmbH</div>
    </footer>
  </section>

  <section class="page page--back">
    <div class="top-band"><span></span><span></span></div>
    <div class="letter">
      <p class="salutation">Sehr geehrte Damen und Herren,</p>
      <p>gerne bewerben wir uns als freier Mitarbeiter im Rahmen des § 17 BOStB für Ihre Kanzlei.</p>
      <p>Gerne übernehmen wir für Sie im Rahmen der freien Mitarbeiter:</p>
      <ul class="services">
        <li>FINANZBUCHHALTUNG</li>
        <li>LOHNBUCHHALTUNG (AUCH BAULOHN)</li>
        <li>JAHRESABSCHLUSS</li>
        <li>STEUERERKLÄRUNGEN</li>
      </ul>
      <p>Fachliche Erfahrungen bestehen seit über 20 Jahren. Die Tätigkeit auf diversen branchenübli&shy;chen Abrechnungsprogrammen ist uns vertraut.</p>
      <p>Mit freundlichen Grüßen</p>
      <div class="signature">Jonas Berger</div>
    </div>
    <footer class="back-foot">
      <div>Kontowerk GmbH • Lindenstraße 12</div>
      <div>70173 Musterstadt •
        <svg class="icon" width="6" height="7" viewBox="0 0 6 7"><path d="M1 0.5 L2.2 0.5 L2.6 2 L1.8 2.6 Q2.3 4 3.4 4.7 L4 3.9 L5.5 4.3 L5.5 5.5 Q3 6.8 1 3.8 Q0.3 2 1 0.5Z" fill="#fff"/></svg>0711/5550123</div>
      <div><svg class="icon" width="8" height="6" viewBox="0 0 8 6"><rect x=".4" y=".4" width="7.2" height="5.2" fill="none" stroke="#fff" stroke-width=".7"/><path d="M.4 .4 L4 3.2 L7.6 .4" fill="none" stroke="#fff" stroke-width=".7"/></svg>info@kontowerk-beispiel.de</div>
    </footer>
  </section>
</body>
</html>
```